Upcoming author needs a book cover design (first in a trilogy)

I need a book cover design for my first novel. It is not yet published and I would like to present the book, complete with a cover to potential publishers. In the interim I would like to be able to use the cover as visual motivation to get it published.
The novel is called 'Burnt Maple Hours' and my pen name is Miriam Dowse. It is a novel set in an Australian beachside town,and is about developing tenacity and courage in the face of fear - aimed at the Young adult market.
I want the cover to be text only (no images) and I really like the old school chalkboard design style. I particularly like the colours turquoise, fuschia pink and canary yellow together. As this is the first of 3 books, I would like the design, fonts and colours to be able to be stepped across all three covers...with one colour used predominently in each cover. For Burnt Maple, I would like the Turquoise blue to be the strongest colour.
I would like the cover to somehow reflect the fact that the story is set by and in the ocean without appearing 'cute/kitsch' at all.
Hello Designers,
Target Market(s)
Young adult readers - most books aimed here are black covers with dark print and imagery. I want this to be light, bright and really stand out on the shelves.
Industry/Entity Type
School
Requirements
Must have
- Ability to be printed out as A2
Should not have
- Images

```html
<!DOCTYPE html>
<html lang="en">
<head>
<meta charset="utf-8">
<title>Burnt Maple Hours – Cover Concepts</title>
<link rel="stylesheet" href="https://fonts.googleapis.com/css2?family=Rokkitt:wght@800&family=Rubik+Distressed&display=swap">
<style>
  :root {
    --turquoise: #00cbff;
    --turquoise-light: #7fe4ff;
    --fuchsia: #d300ab;
    --violet: #8e44cf;
    --coral: #f0664c;
    --canary: #ffcc00;
    --white: #ffffff;
  }
  html, body {
    margin: 0;
    padding: 0;
    width: 1200px;
    height: 1000px;
    overflow: hidden;
    background: var(--white);
  }
  .stage {
    position: relative;
    width: 1200px;
    height: 1000px;
  }
  .cover {
    position: absolute;
    top: 201px;
    width: 421px;
    height: 595px;
    overflow: hidden;
  }
  .cover--back { left: 130px; background: var(--fuchsia); }
  .cover--front { left: 645px; background: var(--turquoise); }
  .band { position: absolute; left: 0; width: 100%; z-index: 0; }
  .band--turquoise { background: var(--turquoise); }
  .band--violet { background: var(--violet); }
  .band--fuchsia { background: var(--fuchsia); }
  .band--coral { background: var(--coral); }
  .band--canary { background: var(--canary); }
  .band--white { background: var(--white); }
  .moon {
    position: absolute;
    left: 321px;
    top: 49px;
    width: 196px;
    height: 196px;
    border-radius: 50%;
    background: var(--turquoise-light);
  }
  .author {
    position: absolute;
    z-index: 1;
    left: 11px;
    top: 310px;
    margin: 0;
    font-family: "Rokkitt", Georgia, serif;
    font-weight: 800;
    font-size: 29px;
    line-height: 1;
    color: var(--white);
    letter-spacing: 0.3px;
    white-space: nowrap;
  }
  .title {
    position: absolute;
    z-index: 1;
    right: 16px;
    top: 352px;
    margin: 0;
    font-family: "Rubik Distressed", Impact, sans-serif;
    font-weight: 400;
    font-size: 54px;
    line-height: 73px;
    text-align: right;
    color: var(--white);
    white-space: nowrap;
  }
</style>
</head>
<body>
<main class="stage">
  <section class="cover cover--back" aria-label="Back cover">
    <div class="band band--turquoise" style="top:0;height:45px"></div>
    <div class="band band--violet" style="top:45px;height:12px"></div>
    <div class="band band--white" style="top:288px;height:20px"></div>
    <p class="author">Miriam Dowse</p>
    <div class="band band--coral" style="top:539px;height:11px"></div>
    <div class="band band--canary" style="top:550px;height:45px"></div>
  </section>

  <section class="cover cover--front" aria-label="Front cover">
    <div class="moon"></div>
    <div class="band band--white" style="top:288px;height:20px"></div>
    <p class="author">Miriam Dowse</p>
    <h1 class="title">Burnt Maple<br>Hours</h1>
    <div class="band band--violet" style="top:494px;height:12px"></div>
    <div class="band band--fuchsia" style="top:506px;height:33px"></div>
    <div class="band band--coral" style="top:539px;height:11px"></div>
    <div class="band band--canary" style="top:550px;height:45px"></div>
  </section>
</main>
</body>
</html>
```